EOFY Sale

please redesign these 2 ads for Vexo advertising - use same concept and design but make it look better. our website is www.kelvaroutfitterhomes.com.au for more info.

```html
<!DOCTYPE html>
<html lang="en">
<head>
<meta charset="utf-8">
<title>Kelvar Homes – EOFY Sale</title>
<link rel="stylesheet" href="https://fonts.googleapis.com/css2?family=Anton&family=Barlow+Condensed:ital,wght@1,700&family=Montserrat:wght@800;900&family=Poppins:wght@400;500;600;700&display=swap">
<style>
  :root{
    --red:#e8262f;
    --blue:#1570b8;
    --blue-deep:#0f4f86;
    --label-blue:#1466a8;
    --black:#1a1a1a;
    --yellow:#ffd200;
    --white:#ffffff;
    --gold:#d9a431;
  }
  *{box-sizing:border-box;margin:0;padding:0}
  html,body{width:1164px;height:1200px;overflow:hidden;background:var(--white)}
  body{position:relative;font-family:"Poppins",sans-serif}
  .abs{position:absolute}

  /* hero */
  .hero-backdrop{left:0;top:0;width:1164px;height:444px;background:linear-gradient(120deg,#f2f2f2 0%,#e2e3e4 50%,#f4f4f4 100%)}
  .hero-photo{left:0;top:0;width:370px;height:444px}
  .badge{left:287px;top:132px;width:172px;height:172px}
  .price-tag{left:534px;top:160px;width:120px;height:60px;transform:rotate(-55deg);transform-origin:center}
  .price-tag .tag-body{position:absolute;inset:0;background:var(--yellow);clip-path:polygon(18% 0,100% 0,100% 100%,18% 100%,0 50%);display:flex;align-items:center;justify-content:center;padding-left:14px;font-family:"Montserrat",sans-serif;font-weight:900;font-size:34px;color:var(--blue);letter-spacing:-1px}
  .headline-fifty{left:648px;top:34px;font-family:"Anton",sans-serif;font-size:268px;line-height:1;color:var(--red);letter-spacing:-6px}
  .headline-percent{left:927px;top:50px;font-family:"Anton",sans-serif;font-size:170px;line-height:1;color:var(--red)}
  .headline-off{left:943px;top:213px;font-family:"Montserrat",sans-serif;font-weight:900;font-size:54px;line-height:1;color:var(--red)}
  .headline-all{left:558px;top:280px;font-family:"Montserrat",sans-serif;font-weight:900;font-size:86px;line-height:1;color:#111;letter-spacing:-2px;white-space:nowrap}
  .tagline-band{left:0;top:381px;width:1164px;height:63px;background:var(--red);clip-path:polygon(307px 0,1164px 0,1164px 100%,268px 100%)}
  .tagline{left:325px;top:393px;font-weight:600;font-size:31px;color:var(--white);white-space:nowrap;letter-spacing:-.2px}

  /* blue categories */
  .category-band{left:0;top:443px;width:1164px;height:274px;background:var(--blue)}
  .category{top:482px;display:flex;align-items:center;gap:24px}
  .category-icon{width:102px;height:102px;border-radius:50%;background:var(--blue-deep);border:3px solid var(--white);display:flex;align-items:center;justify-content:center}
  .category-name{font-family:"Barlow Condensed",sans-serif;font-style:italic;font-weight:700;font-size:44px;line-height:38px;color:var(--white)}

  /* product cards */
  .card{width:253px;background:var(--white);padding:6px;box-shadow:0 2px 6px rgba(0,0,0,.15)}
  .card .photo{width:100%}
  .card .label{background:var(--label-blue);color:var(--white);font-weight:700;font-size:15px;text-align:center;height:37px;line-height:37px;white-space:nowrap}
  .row-top .card{top:631px;height:162px}
  .row-top .photo{height:114px}
  .row-bottom .card{top:833px;height:167px}
  .row-bottom .photo{height:113px}
  .row-bottom .label{height:40px;line-height:40px}

  .ribbon{position:absolute;left:38px;top:-22px;width:172px;height:54px;background:var(--red);transform:rotate(-4deg) skewX(-10deg);box-shadow:0 3px 6px rgba(0,0,0,.25)}
  .ribbon-content{position:absolute;inset:0;transform:skewX(10deg);color:var(--white)}
  .ribbon .small{position:absolute;left:28px;top:4px;font-weight:700;font-size:10px;line-height:1;z-index:1}
  .ribbon-inner{position:absolute;left:26px;top:15px;display:flex;align-items:flex-end;gap:4px;line-height:1}
  .ribbon .big{font-family:"Anton",sans-serif;font-size:34px;line-height:34px;color:var(--yellow)}
  .ribbon .off{font-weight:700;font-size:20px;line-height:20px;padding-bottom:4px}
  .ribbon .from-price{font-family:"Anton",sans-serif;font-size:30px;line-height:32px;color:var(--yellow)}
  .ribbon .per{font-weight:700;font-size:15px;line-height:14px;text-align:center;padding-bottom:3px;margin-top:-8px}

  .sticker{position:absolute;right:-10px;top:-18px;width:66px;height:66px;border-radius:50%;background:var(--red);color:var(--white);text-align:center;box-shadow:0 2px 5px rgba(0,0,0,.3);overflow:hidden}
  .sticker::after{content:"";position:absolute;right:-6px;top:-6px;width:30px;height:30px;background:#f1f1f1;border-radius:0 0 0 30px;box-shadow:-2px 2px 3px rgba(0,0,0,.2)}
  .sticker .small{display:block;font-size:8px;font-weight:700;margin-top:14px;line-height:1}
  .sticker .big{display:block;font-family:"Anton",sans-serif;font-size:26px;color:var(--yellow);line-height:1}

  /* footer */
  .footer-band{left:0;top:918px;width:1164px;height:282px;background:var(--black)}
  .white-gap{left:0;top:717px;width:1164px;height:201px;background:var(--white)}
  .brand{left:60px;top:1083px;display:flex;align-items:center;gap:8px}
  .brand-mark{width:16px;height:16px;background:var(--red)}
  .brand-name{font-weight:700;font-size:22px;line-height:1;color:var(--blue);white-space:nowrap}
  .address{left:263px;top:1069px;width:424px;height:33px;background:var(--red);border-radius:4px;display:flex;align-items:center;gap:6px;padding-left:8px;color:var(--white);font-size:18px;white-space:nowrap}
  .hours{left:263px;top:1114px;display:flex;align-items:center;gap:6px;color:var(--white);font-size:15px;white-space:nowrap}
  .hours .gap{width:10px}
  .divider{left:715px;top:1070px;width:2px;height:72px;background:var(--white)}
  .phone{left:740px;top:1058px;display:flex;align-items:center;gap:12px;color:var(--white);font-weight:700;font-size:50px;line-height:1;white-space:nowrap}
  .website{left:740px;top:1117px;color:var(--white);font-size:19px;font-weight:500;white-space:nowrap}
  .website b{color:var(--yellow);font-weight:600}
</style>
</head>
<body>

<div class="abs hero-backdrop" role="img" aria-label="Soft grey photo of a bright backyard patio"></div>

<svg class="abs hero-photo" viewBox="0 0 370 444">
  <defs>
    <linearGradient id="patioTone" x1="0" y1="0" x2="0" y2="1">
      <stop offset="0" stop-color="#b08a5e"/>
      <stop offset=".3" stop-color="#55604f"/>
      <stop offset=".6" stop-color="#6f7a5a"/>
      <stop offset="1" stop-color="#9a9a96"/>
    </linearGradient>
  </defs>
  <polygon points="270,0 364,122 311,381 268,444 0,444 0,0" fill="var(--blue)"/>
  <polygon points="258,0 352,122 300,381 262,444 0,444 0,0" fill="url(#patioTone)" role="img" aria-label="Photo of a covered outdoor patio with a drop-down screen blind"/>
</svg>

<svg class="abs badge" viewBox="0 0 172 172">
  <defs>
    <radialGradient id="goldTone" cx=".4" cy=".35" r=".7">
      <stop offset="0" stop-color="#ffe7a0"/>
      <stop offset=".6" stop-color="#d9a431"/>
      <stop offset="1" stop-color="#a8741c"/>
    </radialGradient>
  </defs>
  <circle cx="86" cy="86" r="84" fill="url(#goldTone)"/>
  <circle cx="86" cy="86" r="70" fill="#f3c55a"/>
  <circle cx="86" cy="86" r="60" fill="#6b0f10"/>
  <text x="86" y="62" text-anchor="middle" font-family="Poppins,sans-serif" font-weight="600" font-size="13" fill="#fff">Celebrating</text>
  <text x="86" y="104" text-anchor="middle" font-family="Anton,sans-serif" font-size="46" fill="#f4c14f">10</text>
  <text x="86" y="112" text-anchor="middle" font-family="Poppins,sans-serif" font-style="italic" font-size="13" fill="#fff">years</text>
  <text x="86" y="127" text-anchor="middle" font-family="Poppins,sans-serif" font-weight="700" font-size="11" fill="#fff">IN BUSINESS</text>
  <circle cx="20" cy="86" r="3" fill="#6b0f10"/>
  <circle cx="152" cy="86" r="3" fill="#6b0f10"/>
</svg>

<div class="abs price-tag"><div class="tag-body">UPTO</div></div>
<div class="abs headline-fifty">50</div>
<div class="abs headline-percent">%</div>
<div class="abs headline-off">OFF</div>
<div class="abs headline-all">ALL BLINDS</div>

<div class="abs tagline-band"></div>
<div class="abs tagline">INDOORS OR OUTDOORS WE'VE GOT U COVERED</div>

<div class="abs category-band"></div>
<div class="abs white-gap"></div>
<div class="abs footer-band"></div>

<div class="abs category" style="left:60px">
  <div class="category-icon">
    <svg width="54" height="60" viewBox="0 0 54 60" fill="none" stroke="#fff" stroke-width="3">
      <rect x="6" y="4" width="42" height="52"/>
      <line x1="6" y1="12" x2="48" y2="12"/><line x1="6" y1="19" x2="48" y2="19"/><line x1="6" y1="26" x2="48" y2="26"/>
      <rect x="12" y="32" width="30" height="22"/>
      <line x1="48" y1="8" x2="48" y2="30"/>
    </svg>
  </div>
  <div class="category-name">INDOOR<br>BLINDS</div>
</div>
<div class="abs category" style="left:423px">
  <div class="category-icon">
    <svg width="60" height="54" viewBox="0 0 60 54" fill="none" stroke="#fff" stroke-width="3">
      <rect x="4" y="4" width="52" height="46"/>
      <line x1="4" y1="12" x2="56" y2="12"/><line x1="4" y1="20" x2="56" y2="20"/><line x1="4" y1="28" x2="56" y2="28"/>
      <line x1="30" y1="32" x2="30" y2="50"/>
    </svg>
  </div>
  <div class="category-name">OUTDOOR<br>BLINDS</div>
</div>
<div class="abs category" style="left:790px">
  <div class="category-icon">
    <svg width="60" height="54" viewBox="0 0 60 54" fill="#fff" stroke="#fff" stroke-width="3">
      <line x1="2" y1="4" x2="58" y2="4"/>
      <path d="M6 6 Q14 24 10 50 L18 50 Q18 28 26 6 Z" stroke="none"/>
      <path d="M54 6 Q46 24 50 50 L42 50 Q42 28 34 6 Z" stroke="none"/>
    </svg>
  </div>
  <div class="category-name">SHEERS &amp;<br>CURTAINS</div>
</div>

<div class="row-top">
  <div class="abs card" style="left:59px">
    <div class="photo" role="img" aria-label="Photo of a timber deck with outdoor zip screen blinds" style="background:linear-gradient(180deg,#6e6e6a,#a9a49a 55%,#9c5a33)"></div>
    <div class="label">SLIDELOCK &amp; ZIPSCREEN BLINDS</div>
    <div class="ribbon"><div class="ribbon-content"><span class="small">UP TO</span><div class="ribbon-inner"><span class="big">50%</span><span class="off">OFF</span></div></div></div>
  </div>
  <div class="abs card" style="left:324px">
    <div class="photo" role="img" aria-label="Photo of a window fitted with roller shutters" style="background:linear-gradient(180deg,#333,#555 60%,#ddd)"></div>
    <div class="label">ROLLER SHUTTERS</div>
    <div class="ribbon"><div class="ribbon-content"><span class="small">UP TO</span><div class="ribbon-inner"><span class="big">50%</span><span class="off">OFF</span></div></div></div>
  </div>
  <div class="abs card" style="left:588px">
    <div class="photo" role="img" aria-label="Photo of a bedroom with white plantation shutters" style="background:linear-gradient(180deg,#e4e4e2,#cfcfcc 60%,#8a8a88)"></div>
    <div class="label">PVC PLANTATION SHUTTERS</div>
    <div class="ribbon"><div class="ribbon-content"><span class="small">FROM</span><div class="ribbon-inner"><span class="from-price">$299</span><span class="per">PER<br>SQM2</span></div></div></div>
  </div>
  <div class="abs card" style="left:852px">
    <div class="photo" role="img" aria-label="Photo of a living room with dark roller blinds" style="background:linear-gradient(90deg,#6a4a35,#2a2a2a 40%,#8a6a50 70%,#cfd6d0)"></div>
    <div class="label">ROLLER BLINDS</div>
    <div class="ribbon"><div class="ribbon-content"><span class="small">UP TO</span><div class="ribbon-inner"><span class="big">50%</span><span class="off">OFF</span></div></div></div>
  </div>
</div>

<div class="row-bottom">
  <div class="abs card" style="left:59px">
    <div class="photo" role="img" aria-label="Photo of an outdoor awning over a garden lounge" style="background:linear-gradient(180deg,#9a5a32,#4e7a3e 45%,#8a8a84)"></div>
    <div class="label">OUTDOOR AWNINGS</div>
    <div class="sticker"><span class="small">UP TO</span><span class="big">50%</span></div>
  </div>
  <div class="abs card" style="left:324px">
    <div class="photo" role="img" aria-label="Photo of a lounge room with sheer drapes" style="background:linear-gradient(180deg,#e8e6e2,#c9c2b6 60%,#7a5a3a)"></div>
    <div class="label">SHEERS &amp; DRAPES</div>
    <div class="sticker"><span class="small">UP TO</span><span class="big">50%</span></div>
  </div>
  <div class="abs card" style="left:588px">
    <div class="photo" role="img" aria-label="Photo of a room with soft sheer shade blinds" style="background:linear-gradient(180deg,#f0efec,#dedcd8 60%,#b9b6b0)"></div>
    <div class="label">VISTA SHADE BLINDS</div>
    <div class="sticker"><span class="small">UP TO</span><span class="big">50%</span></div>
  </div>
  <div class="abs card" style="left:852px">
    <div class="photo" role="img" aria-label="Photo of white venetian blinds over a leafy window" style="background:linear-gradient(180deg,#f4f4f2,#8fc070 55%,#e6ece2)"></div>
    <div class="label">VENETIAN BLINDS</div>
    <div class="sticker"><span class="small">UP TO</span><span class="big">50%</span></div>
  </div>
</div>

<div class="abs brand"><span class="brand-mark"></span><span class="brand-name">Kelvar Homes</span></div>

<div class="abs address">
  <svg width="16" height="20" viewBox="0 0 16 20"><path d="M8 0C3.6 0 0 3.4 0 7.6 0 13 8 20 8 20s8-7 8-12.4C16 3.4 12.4 0 8 0z" fill="var(--yellow)"/><circle cx="8" cy="7.5" r="3" fill="var(--red)"/></svg>
  48 Larkspur Avenue, Brindlewood
</div>

<div class="abs hours">
  <svg width="13" height="13" viewBox="0 0 13 13"><rect x="1" y="2" width="11" height="10" fill="none" stroke="var(--yellow)" stroke-width="1.6"/><line x1="1" y1="5" x2="12" y2="5" stroke="var(--yellow)" stroke-width="1.6"/></svg>MON-FRI<span class="gap"></span>
  <svg width="13" height="13" viewBox="0 0 13 13"><circle cx="6.5" cy="6.5" r="5.5" fill="var(--yellow)"/><path d="M6.5 3.5V6.5H9" stroke="var(--black)" stroke-width="1.4" fill="none"/></svg>9am-5pm<span class="gap"></span>
  <svg width="13" height="13" viewBox="0 0 13 13"><rect x="1" y="2" width="11" height="10" fill="none" stroke="var(--yellow)" stroke-width="1.6"/><line x1="1" y1="5" x2="12" y2="5" stroke="var(--yellow)" stroke-width="1.6"/></svg>SATURDAY<span class="gap"></span>
  <svg width="13" height="13" viewBox="0 0 13 13"><circle cx="6.5" cy="6.5" r="5.5" fill="var(--yellow)"/><path d="M6.5 3.5V6.5H9" stroke="var(--black)" stroke-width="1.4" fill="none"/></svg>10am-4pm
</div>

<div class="abs divider"></div>

<div class="abs phone">
  <svg width="34" height="34" viewBox="0 0 24 24"><path d="M6.6 10.8a15.1 15.1 0 006.6 6.6l2.2-2.2c.3-.3.7-.4 1-.2 1.1.4 2.3.6 3.6.6.6 0 1 .4 1 1V20c0 .6-.4 1-1 1C10.6 21 3 13.4 3 4c0-.6.4-1 1-1h3.5c.6 0 1 .4 1 1 0 1.3.2 2.5.6 3.6.1.3 0 .7-.2 1z" fill="var(--yellow)"/></svg>
  03 5550 1287
</div>
<div class="abs website">www.<b>kelvaroutfitterhomes</b>.com.au</div>

</body>
</html>
```